Webdesign für Automotive Engineering Webpage
Automotive Engineering - Main focus is Software Development & Embedded systems for the Automotive industry.
Like as HMI, ADAS, ECU
See Logo (PDF), example --> https://www.brantlex.com/de/de (competetor)

```html
<!DOCTYPE html>
<html lang="de">
<head>
<meta charset="utf-8">
<title>VELTRON – Automotive Engineering &amp; Consulting Solutions</title>
<link href="https://fonts.googleapis.com/css2?family=Oswald:wght@500&family=Lato:wght@400;700&display=swap" rel="stylesheet">
<style>
:root{
  --navy:#0b2a5b;
  --red:#e3262b;
  --ink:#2b2b2b;
  --text:#3b3b3b;
  --muted:#7a8aa6;
  --topbar:#2e3038;
  --rule:#e4e4e8;
  --white:#ffffff;
}
*{box-sizing:border-box;margin:0;padding:0}
html,body{width:1200px;height:3722px;overflow:hidden;background:var(--white)}
body{font-family:"Lato",sans-serif;color:var(--text);position:relative}
.abs{position:absolute}
h1,h2{font-family:"Oswald",sans-serif;font-weight:500;color:var(--ink)}
.eyebrow{font-size:11px;letter-spacing:2px;text-transform:uppercase;color:var(--muted)}
.btn{display:inline-flex;align-items:center;justify-content:center;font-size:11px;letter-spacing:2px;text-transform:uppercase;border:1.5px solid var(--navy);color:var(--navy);background:var(--white)}
.btn.solid{background:var(--navy);color:var(--white)}
.rule{position:absolute;left:100px;width:999px;height:3px;background:var(--rule)}
p.copy{font-size:12.5px;line-height:18.5px;margin-bottom:18px}

.topbar{top:0;left:0;width:1200px;height:37px;background:var(--topbar);color:#e8e8ee;font-size:11px;letter-spacing:1.5px}
.topbar .phone{left:100px;top:12px;display:flex;gap:6px;align-items:center}
.topbar .menu{right:100px;top:12px;display:flex;gap:12px}

.header{top:37px;left:0;width:1200px;height:102px;background:var(--white)}
.brand{font-family:"Lato",sans-serif;font-weight:700;color:var(--navy);font-size:26px;letter-spacing:2px;display:flex;align-items:center;gap:8px}
.brand .dot{width:12px;height:12px;background:var(--red);border-radius:50%}
.header .brand{left:100px;top:36px}
.nav{right:100px;top:42px;display:flex;gap:20px;font-size:11.5px;letter-spacing:2px;color:#333}

.hero{top:139px;left:0;width:1200px;height:572px;background:linear-gradient(135deg,#4b5a72 0%,#6d7f99 40%,#55627a 70%,#3b4559 100%)}
.hero .band{left:0;top:122px;width:1200px;height:236px;background:rgba(40,46,62,.55)}
.hero .label{top:143px;width:1200px;text-align:center;color:#e8eaf0;font-size:11px;letter-spacing:2px}
.hero h1{top:168px;width:1200px;text-align:center;color:var(--white);font-size:51px;line-height:56px}
.hero .btn{left:502px;top:299px;width:195px;height:38px;background:transparent;color:var(--white);border-color:rgba(255,255,255,.8)}
.hero .social{left:102px;top:500px;display:flex;gap:28px}
.hero .social span{width:32px;height:32px;background:rgba(255,255,255,.85);border-radius:4px}

.services h2{top:793px;width:1200px;text-align:center;font-size:30px}
.services .sub{top:850px;width:1200px;text-align:center;font-size:13px}
.card{top:898px;width:208px;height:243px;background:var(--white);border:1.5px solid #d9dbe3;padding:20px 27px}
.card.raised{box-shadow:0 4px 10px rgba(0,0,0,.15)}
.card .icon{width:30px;height:26px;margin-bottom:12px;display:block}
.card h3{font-family:"Lato",sans-serif;font-weight:400;font-size:16px;line-height:20px;color:var(--ink);padding-bottom:8px;border-bottom:1px solid var(--rule);margin-bottom:16px;height:50px;overflow-wrap:anywhere}
.card p{font-size:11px;line-height:18px;height:60px}
.card .btn{width:152px;height:30px;margin-top:12px}

.originate h2{left:100px;top:1337px;font-size:31px}
.originate .body{left:100px;top:1396px;width:556px}
.originate .btn{left:100px;top:1674px;width:152px;height:30px}
.frame{background:var(--navy)}
.photo{background:linear-gradient(160deg,#c9ced6 0%,#8d96a4 50%,#3f4a5c 100%)}

.about .eyebrow{left:507px;top:1912px}
.about h2{left:507px;top:1933px;font-size:31px}
.about .body{left:507px;top:1994px;width:593px}

.apply .eyebrow{left:100px;top:2509px}
.apply h2{left:100px;top:2534px;width:960px;font-size:31px;line-height:36px}
.apply .body{left:100px;top:2636px;width:890px}
.apply a{color:var(--red);text-decoration:none}

.contact{top:2954px;left:0;width:1200px;height:454px;background:var(--navy);overflow:hidden}
.contact .eyebrow{left:100px;top:80px;color:#9fb0cc}
.contact h2{left:100px;top:106px;width:440px;color:var(--white);font-size:30px;line-height:36px}
.contact .lead{left:100px;top:233px;width:360px;color:var(--white);font-size:12.5px;line-height:18.5px}
.field{left:635px;width:464px;height:38px;background:var(--white);font-size:12px;color:#9aa8c2;padding:0 12px;display:flex;align-items:center}
.contact .send{left:635px;top:333px;width:182px;height:38px;background:var(--red);color:var(--white);font-size:11px;letter-spacing:2px;display:flex;align-items:center;justify-content:center}

.footer{top:3408px;left:0;width:1200px;height:272px}
.footer .brand{left:100px;top:66px;font-size:30px}
.footer .social{left:100px;top:167px;display:flex;gap:16px}
.footer .social span{width:20px;height:20px;background:var(--navy);border-radius:3px}
.fcol{top:62px}
.fcol h4{font-family:"Lato",sans-serif;font-weight:700;font-size:14px;color:var(--ink);margin-bottom:18px}
.fcol li{list-style:none;font-size:12.5px;line-height:26.5px;color:var(--ink)}
.addr{font-size:11px;line-height:18px;color:var(--ink)}
.addr .row{display:flex;gap:12px}
.addr svg{flex:0 0 14px;margin-top:3px}
.bottombar{top:3680px;left:0;width:1200px;height:42px;background:var(--red);color:var(--white);font-size:11px}
.bottombar .l{left:100px;top:15px}
.bottombar .r{right:100px;top:15px}
</style>
</head>
<body>

<div class="abs topbar">
  <div class="abs phone"><svg width="11" height="11" viewBox="0 0 24 24"><path fill="#e8e8ee" d="M6.6 10.8a15 15 0 0 0 6.6 6.6l2.2-2.2c.3-.3.7-.4 1-.2 1.1.4 2.3.6 3.6.6.6 0 1 .4 1 1V20c0 .6-.4 1-1 1A17 17 0 0 1 3 4c0-.6.4-1 1-1h3.5c.6 0 1 .4 1 1 0 1.3.2 2.5.6 3.6.1.3 0 .7-.2 1z"/></svg>+49 (0)4321 - 555 01 23</div>
  <div class="abs menu"><span>KUNDENSERVICE ▾</span><span>ANMELDEN ▾</span></div>
</div>

<header class="abs header">
  <div class="abs brand"><span class="dot"></span>VELTRON</div>
  <nav class="abs nav"><span>LEISTUNGEN</span><span>PROJEKTE/VAKANZEN</span><span>ÜBER UNS</span><span>BEDARFSANFRAGE</span></nav>
</header>

<section class="abs hero" role="img" aria-label="Automobilfertigung mit Industrierobotern an einer Karosserie">
  <div class="abs band"></div>
  <div class="abs label">TRENDS</div>
  <h1 class="abs">Automotive Engineering &amp;<br>Consulting Solutions</h1>
  <div class="abs btn">Zur Projektübersicht</div>
  <div class="abs social"><span></span><span></span><span></span><span></span></div>
</section>

<section class="services">
  <h2 class="abs">Unsere Leistungen</h2>
  <div class="abs sub">There are many reasons to get down and start to get depressed about your situation.</div>

  <div class="abs card raised" style="left:261px">
    <svg class="icon" viewBox="0 0 30 26"><rect x="3" y="8" width="22" height="14" fill="var(--red)"/><rect x="9" y="4" width="8" height="4" fill="var(--red)"/><rect x="0" y="12" width="3" height="6" fill="var(--red)"/><rect x="25" y="11" width="5" height="8" fill="var(--red)"/></svg>
    <h3>Full Service<br>Engineering</h3>
    <p>Übernahme kompletter<br>R&amp;D Projekte als<br>Fremdleistung</p>
    <div class="btn solid">Weiterlesen</div>
  </div>
  <div class="abs card" style="left:497px">
    <svg class="icon" viewBox="0 0 30 26"><rect x="0" y="3" width="30" height="22" rx="2" fill="var(--red)"/><circle cx="9" cy="12" r="3" fill="#fff"/><rect x="5" y="16" width="8" height="4" fill="#fff"/><rect x="16" y="10" width="10" height="2" fill="#fff"/><rect x="16" y="15" width="10" height="2" fill="#fff"/></svg>
    <h3>Premium<br>Recruiting</h3>
    <p>Vermittlung bis hin zum Onboarding von Freelancern und Festangestellten</p>
    <div class="btn">Weiterlesen</div>
  </div>
  <div class="abs card" style="left:731px">
    <svg class="icon" viewBox="0 0 30 26"><circle cx="9" cy="6" r="4" fill="var(--red)"/><circle cx="21" cy="9" r="4" fill="var(--red)"/><rect x="2" y="12" width="14" height="12" rx="3" fill="var(--red)"/><rect x="15" y="15" width="13" height="9" rx="3" fill="var(--red)"/></svg>
    <h3>Arbeitnehmerüberl<br>assung</h3>
    <p>Automotive R&amp;D Experten und Ingenieure in Zeitarbeit</p>
    <div class="btn">Weiterlesen</div>
  </div>
</section>

<div class="rule" style="top:1238px"></div>

<section class="originate">
  <h2 class="abs">Originate in Engineering</h2>
  <div class="abs body">
    <p class="copy">Halvar Recruitment vereint in sich 25 Jahre Branchen- und Projekterfahrung vom Freelance Ingenieur bis zum Task Force Manager in den Branchen Automotive, Schienenfahrzeuge, Luft- und Raumfahrt, Rüstung und Informationstechnologie.</p>
    <p class="copy">Firmengründer und Geschäftsführer Bernd Halvar kennt die Industrie seit über zwei Jahrzehnten, in denen er in Positionen als IT Entwicklungsingenieur, Experte für Geodaten und rund um das Thema autonomes Fahren und Fahrassistenzsysteme, bis zum CIO und Task Force Manager bei fast allen wichtigen OEMs und Tier1s des Automotive Sektors und anderer Schlüsselindustrien Erfahrungen sammeln konnte.</p>
    <p class="copy">Wie der Firmengründer, so verfügen auch alle maßgeblichen Mitarbeiter bei Halvar Recruitment über diese Double Qualification – wir sprechen Ihre Sprache und wissen, wo Ihr Bedarf liegt, kennen Ihre Abläufe und Prozesse, sind aus eigener Erfahrung heraus im Geschäft.</p>
  </div>
  <div class="abs btn">Weiterlesen</div>
  <div class="abs frame" style="left:765px;top:1356px;width:321px;height:348px"></div>
  <div class="abs" style="left:774px;top:1341px;width:325px;height:346px;background:#fff"></div>
  <div class="abs photo" style="left:782px;top:1341px;width:317px;height:344px" role="img" aria-label="Ingenieurteam arbeitet gemeinsam an einem Laptop in der Entwicklungswerkstatt"></div>
</section>

<div class="rule" style="top:1807px"></div>

<section class="about">
  <div class="abs frame" style="left:100px;top:1958px;width:320px;height:348px"></div>
  <div class="abs" style="left:109px;top:1944px;width:326px;height:350px;background:#fff"></div>
  <div class="abs photo" style="left:117px;top:1944px;width:318px;height:346px;background:linear-gradient(160deg,#4f6a3a 0%,#2f3d26 60%,#1e2433 100%)" role="img" aria-label="Porträt des Firmengründers im Anzug vor grünem Hintergrund"></div>
  <div class="abs eyebrow">Über uns</div>
  <h2 class="abs">Halvar Recruitment</h2>
  <div class="abs body">
    <p class="copy">Halvar Recruitment wurde im Jahr 2018 von Bernd Halvar gegründet. Er wusste nach mehr als zwei Jahrzehnten Erfahrung, vorrangig als R&amp;D Ingenieur und Key Manager in der Automotive Industrie, wo der größte Bedarf der Branche liegt: Im Abarbeiten von Bedarfsspitzen mit qualifizierten Mitarbeitern für die Bereiche R&amp;D, IT und Engineering, abhängig von den jeweiligen offenen Projekten. Zudem konnte er miterleben, wie langwierige Recruitment-Prozesse und Auswahlverfahren anderweitig dringend benötigte Kapazitäten im Unternehmen binden und die erfolgskritischen Projekte zusätzlich verzögern.</p>
    <p class="copy">Klassische Personaldienstleister haben sicherlich das HR Thema gut im Griff, können aber auf Grund mangelnder Kenntnisse über Abläufe und Anforderungen in den Kundenprojekten oftmals nicht zielgerichtet und/oder schnell genug qualifiziertes Personal anbieten. Ein weiteres Problem des externen Recruitings ist das fehlende Onboarding und Projekt Boarding, das kundenseitig zusätzlich Kapazitäten bindet.</p>
    <p class="copy">Durch seine fachliche Kompetenz, sein internes Wissen über Projekte und Prozesse wie auch durch seine jahrzehntelange Erfahrung mit Recruitment und Personalführung auf Kundenseite startete er so sein Business als spezialisierter Lösungsanbieter für Automotive Engineering Consulting.</p>
  </div>
</section>

<div class="rule" style="top:2431px"></div>

<section class="apply">
  <div class="abs eyebrow">Bewerber</div>
  <h2 class="abs">Konzentrieren Sie sich auf Ihre Kernkompetenzen – wir konzentrieren uns auf die richtigen Aufgaben und die richtigen Projekte für Sie!</h2>
  <div class="abs body">
    <p class="copy">Ihr Wissen, Ihre Erfahrung und Ihr Können sind wertvolle Assets. Sie brauchen nur noch die richtigen Verbindungen, um eine finanziell wie emotional befriedigende Arbeit daraus zu kreieren. Genau für letzteres können Sie uns ansprechen. Wir kennen Ihre Situation und Ihre Wünsche aus eigenen, langjährigen Erfahrungen, denn wir kommen aus dem IT- und Engineering-Bereich. Wir haben selbst als Freelancer in Automotive und anderen Schlüsselindustrien gearbeitet und wissen, was Sie suchen!</p>
    <p class="copy">Wir vermitteln Sie als Freelancer oder festangestellt projekt- oder zeitbezogen an Ihre Wunschpartner in der Industrie. Wenn Sie in einem festen Arbeitsverhältnis oder im Rahmen einer Arbeitnehmerüberlassung angestellt werden wollen, können Sie uns ebenfalls ansprechen. Wir arbeiten zudem international mit den führenden OEMs, Tier-1 und Tier-2 Unternehmen der Automobilindustrie zusammen.</p>
    <p class="copy">Aber bevor Sie uns gleich Ihre Unterlagen schicken, nehmen Sie kurz Kontakt mit uns auf, damit von Anfang an alles passt. Unsere Arbeit lebt von Effektivität und Effizienz und wir wollen weder Ihre, noch die Zeit unserer Kunden mit offenen Fragen oder gar Nachbesserungen verschwenden!</p>
    <p class="copy">Sie wollen sich initativ bewerben? Schicken Sie uns bitte Ihre Unterlagen an <a href="mailto:cv@halvar-recruitment.de">cv@halvar-recruitment.de</a></p>
  </div>
</section>

<section class="abs contact">
  <div class="abs eyebrow">Halvar Recruitment GmbH</div>
  <h2 class="abs">Sie suchen Spezialisten für eine bestimmte Aufgabe, oder möchten mit uns in Kontakt treten?</h2>
  <p class="abs lead">Senden Sie uns zum Beispiel Ihre Anforderungen und wir kommen mit passenden Profilen auf Sie zu, oder nehmen Sie einfach mit uns Kontakt auf und erfahren was wir für Sie tun können.</p>
  <div class="abs field" style="top:102px">Name*</div>
  <div class="abs field" style="top:159px">E-Mail*</div>
  <div class="abs field" style="top:217px">Telefonnummer</div>
  <div class="abs field" style="top:275px">Ort/PLZ*</div>
  <div class="abs send">ANFRAGE ABSENDEN</div>
</section>

<footer class="abs footer">
  <div class="abs brand"><span class="dot"></span>VELTRON</div>
  <div class="abs social"><span></span><span></span><span></span><span></span></div>
  <div class="abs fcol" style="left:386px"><h4>Navigation</h4><ul><li>Leistungen</li><li>Projekte</li><li>Über uns</li><li>Bedarfsanfrage</li></ul></div>
  <div class="abs fcol" style="left:636px"><h4>Kundenservice</h4><ul><li>Registrieren</li><li>Impressum</li><li>Datenschutz</li></ul></div>
  <div class="abs fcol" style="left:887px"><h4>Adresse &amp; Kontakt</h4>
    <div class="addr">
      <div class="row"><svg width="14" height="14" viewBox="0 0 24 24"><path fill="#c3c9d6" d="M12 2a7 7 0 0 0-7 7c0 5 7 13 7 13s7-8 7-13a7 7 0 0 0-7-7zm0 9.5A2.5 2.5 0 1 1 12 6.5a2.5 2.5 0 0 1 0 5z"/></svg><div>Lindenstraße 7<br>D - 12345 Musterstadt (OT Nord)</div></div>
      <div class="row"><svg width="14" height="14" viewBox="0 0 24 24"><path fill="#c3c9d6" d="M6.6 10.8a15 15 0 0 0 6.6 6.6l2.2-2.2c.3-.3.7-.4 1-.2 1.1.4 2.3.6 3.6.6.6 0 1 .4 1 1V20c0 .6-.4 1-1 1A17 17 0 0 1 3 4c0-.6.4-1 1-1h3.5c.6 0 1 .4 1 1 0 1.3.2 2.5.6 3.6.1.3 0 .7-.2 1z"/></svg><div>+49 (0)4321 -555 01 23</div></div>
      <div class="row" style="margin-top:6px"><svg width="14" height="14" viewBox="0 0 24 24"><path fill="#c3c9d6" d="M6 3h12v5H6zM3 9h18v9h-3v3H6v-3H3zm5 6v4h8v-4z"/></svg><div>+49 (0)4321 -555 01 29</div></div>
      <div class="row" style="margin-top:6px"><svg width="14" height="14" viewBox="0 0 24 24"><path fill="#c3c9d6" d="M2 5h20v14H2zm2 2v.5l8 5 8-5V7z"/></svg><div>office@halvar-recruitment.de<br>D-U-N-S Nr. 512009384</div></div>
    </div>
  </div>
</footer>

<div class="abs bottombar">
  <div class="abs l">© 2020 Veltron.com | All rights reserved.</div>
  <div class="abs r">TermsOfUse&nbsp;&nbsp; Privacy</div>
</div>

</body>
</html>
```